Design some Business Cards for Vortelix7

i need a company card, something modern related with web solution.

logo area (i provide the .psd) logo can be melted with background i dont really care.
need contact area:
Name
tittle

web site
email
and phone.

color range: i like dark color modern but dark.

```html
<!DOCTYPE html>
<html lang="en">
<head>
<meta charset="utf-8">
<title>Vortelix7 Business Card</title>
<link rel="stylesheet" href="https://fonts.googleapis.com/css2?family=Open+Sans:wght@300;400&family=Oswald:wght@500;600&display=swap">
<style>
  :root {
    --brand-red: #ff3217;
    --deep-dark: #1c2124;
    --corner-dark: #1a1410;
    --card-white: #ffffff;
    --ink: #1f1f1f;
  }
  * { margin: 0; padding: 0; box-sizing: border-box; }
  html, body { width: 1200px; height: 720px; overflow: hidden; }
  body { background: var(--brand-red); font-family: "Open Sans", Arial, sans-serif; }
  .card-canvas { position: relative; width: 1200px; height: 720px; overflow: hidden; }
  .backdrop { position: absolute; inset: 0; }
  .card-face {
    position: absolute; left: 57px; top: 60px; width: 1083px; height: 600px;
    background: var(--card-white);
  }
  .brand-mark {
    position: absolute; left: 24px; top: 20px; width: 152px; height: 147px;
    background: var(--deep-dark);
  }
  .brand-name {
    position: absolute; left: 212px; top: 22px;
    font-family: "Open Sans", Arial, sans-serif; font-weight: 300;
    font-size: 92px; line-height: 1; color: var(--brand-red); letter-spacing: 1px;
  }
  .person {
    position: absolute; right: 24px; top: 148px; text-align: center;
    font-family: "Oswald", "Arial Narrow", sans-serif; color: var(--ink);
  }
  .person-name { font-size: 44px; font-weight: 600; line-height: 1.1; }
  .person-title { font-size: 27px; font-weight: 500; line-height: 1.2; letter-spacing: .3px; }
  .brand-block {
    position: absolute; left: 23px; top: 396px; width: 181px; height: 173px;
    background: var(--deep-dark);
  }
  .contact-list { position: absolute; list-style: none; color: var(--ink); font-size: 23px; }
  .contact-list li { position: absolute; display: flex; align-items: flex-start; white-space: nowrap; }
  .contact-list svg { width: 24px; height: 24px; margin-right: 14px; margin-top: 4px; flex: none; fill: var(--ink); }
  .contact-main { left: 290px; top: 395px; }
  .contact-side { left: 695px; top: 395px; }
  .address { line-height: 1.95; white-space: normal; width: 260px; }
</style>
</head>
<body>
<main class="card-canvas">
  <svg class="backdrop" width="1200" height="720" viewBox="0 0 1200 720" aria-hidden="true">
    <rect width="1200" height="720" fill="var(--brand-red)"/>
    <polygon points="945,0 1200,0 1200,245" fill="var(--deep-dark)"/>
    <polygon points="918,0 945,0 1200,245 1200,272" fill="#ffffff"/>
    <polygon points="0,372 0,720 348,720" fill="var(--corner-dark)"/>
    <polygon points="0,360 0,372 348,720 362,720" fill="#ffffff"/>
  </svg>

  <section class="card-face">
    <div class="brand-mark"></div>
    <h1 class="brand-name">Vortelix7</h1>

    <div class="person">
      <p class="person-name">R.K</p>
      <p class="person-title">GRAPHIC DESIGNER</p>
    </div>

    <div class="brand-block"></div>
  </section>

  <ul class="contact-list">
    <li class="contact-main" style="left:350px;top:452px">
      <svg viewBox="0 0 24 24"><path d="M7 2h4l-1 6-3 1.5c1 3 3 5.5 6 6.5L14.5 13l6 1v4c0 1-1 2-2 2C9 20 4 13 4 5c0-1.5 1.5-3 3-3z"/></svg>
      +447700 900314
    </li>
    <li class="contact-main" style="left:348px;top:508px">
      <svg viewBox="0 0 24 24"><circle cx="12" cy="12" r="10" fill="none" stroke="#1f1f1f" stroke-width="2"/><path d="M6 6c3 1 4 3 3 5-1 1-3 1-3 3s2 3 2 6M14 3c0 3 3 3 3 6s-3 2-3 5 3 3 4 4"/></svg>
      www.vortelix7.co.uk
    </li>
    <li class="contact-main" style="left:348px;top:565px">
      <svg viewBox="0 0 24 24"><path d="M2 5h20v14H2z" fill="none" stroke="#1f1f1f" stroke-width="2"/><path d="M2 5l10 8 10-8" fill="none" stroke="#1f1f1f" stroke-width="2"/></svg>
      hello@vortelix7.com
    </li>
    <li class="contact-side" style="left:752px;top:453px">
      <svg viewBox="0 0 24 24"><path d="M6 2h12v6H6z"/><path d="M2 9h20v9H2z"/><path d="M6 15h12v7H6z" fill="#fff" stroke="#1f1f1f" stroke-width="2"/></svg>
      1204567893210
    </li>
    <li class="contact-side" style="left:754px;top:502px">
      <svg viewBox="0 0 24 24"><path d="M12 1a8 8 0 0 1 8 8c0 6-8 14-8 14S4 15 4 9a8 8 0 0 1 8-8zm0 5a3 3 0 1 0 0 6 3 3 0 0 0 0-6z"/></svg>
      <span class="address" style="margin-top:-8px;margin-left:-6px">business address will<br>come here</span>
    </li>
  </ul>
</main>
</body>
</html>
```